Daravy's Tralonh - a history of an interesting place

I need a book cover for a project on the history of a province in Cambodia. It is a joint project with Daravy, who is a wheelchair bound local resident from the salt fields. This is a 200 year story told through the lives of his family and ancestors. The photo of the people should be on the back cover. The overall effect should be a historical book which draws people in with the detail of the two main images - map and drawing with the helicopter somewhere - maybe back cover? The title should not obscure the detail in the pictures too much.

Target Market(s)

Visitors to Tralonh who are interested in the place

Font styles to use
Serif

Colors

Designer to choose colors to be used in the design.

Requirements
Must have
• A feel for the past (eg the French colonial map)
Nice to have
• Images of salt fields - the top left part of the drawing has this connection.
Should not have
• I want to avoid the image and perception of war - the helicopter may give a wrong impression - it was dropping food to starving villagers. Perhaps emphasize the map more?

```html
<!DOCTYPE html>
<html lang="en">
<head>
<meta charset="utf-8">
<title>Daravy's Tralonh – Book Cover</title>
<link href="https://fonts.googleapis.com/css2?family=Playfair+Display:wght@600;700;900&family=Lora:wght@400;700&display=swap" rel="stylesheet">
<style>
  :root{
    --teal:#1a93b2;
    --teal-deep:#13788f;
    --sky:#6ec3dc;
    --slate:#4e4f51;
    --ink:#1d1d1d;
    --paper:#ffffff;
    --backdrop:#9a9c9e;
  }
  *{box-sizing:border-box;margin:0;padding:0}
  html,body{width:1200px;height:1200px;overflow:hidden}
  body{background:var(--backdrop);font-family:'Lora',serif;position:relative}

  .spread{position:absolute;left:50px;top:222px;width:1100px;height:756px;display:flex;background:var(--paper)}

  /* back cover */
  .back-cover{position:relative;width:504px;height:100%;background:var(--paper)}
  .back-cover__banner{position:absolute;left:0;top:0;width:100%;height:373px;
    background:linear-gradient(180deg,#5e9fb4 0%,#7cc2d8 45%,var(--sky) 100%)}
  .back-cover__photo{position:absolute;left:40px;top:163px;width:416px;height:308px;background:var(--paper);
    padding:6px;box-shadow:0 1px 4px rgba(0,0,0,.25)}
  .back-cover__photo-fill{width:100%;height:100%;
    background:linear-gradient(180deg,#e8eef0 0%,#cfd9d4 30%,#7f9a5f 42%,#5f7a58 55%,#8a9aa0 75%,#6e7d6f 100%)}
  .back-cover__blurb{position:absolute;left:46px;top:489px;width:410px;color:var(--ink)}
  .back-cover__lead{font-weight:700;font-size:10.3px;line-height:1.35;margin-bottom:10px}
  .back-cover__body{font-weight:400;font-size:8.5px;line-height:1.4;text-align:justify;margin-bottom:6px;color:#2a2a2a}

  /* spine */
  .spine{position:relative;width:92px;height:100%;background:var(--teal)}
  .spine__title{position:absolute;left:50%;top:40px;transform-origin:0 0;transform:translateX(20px) rotate(90deg);
    white-space:nowrap;color:var(--paper);font-family:'Playfair Display',serif;font-weight:900;font-size:38px;line-height:1}
  .spine__authors{position:absolute;left:50%;top:556px;transform-origin:0 0;transform:translateX(10px) rotate(90deg);
    white-space:nowrap;color:var(--paper);font-family:'Playfair Display',serif;font-weight:700;font-size:15px;line-height:1.15}

  /* front cover */
  .front-cover{position:relative;width:504px;height:100%;background:linear-gradient(180deg,#fff 0%,#fff 85%,#f4f4f4 100%)}
  .front-cover__title{position:absolute;left:0;top:38px;width:100%;text-align:center;color:var(--teal);
    font-family:'Playfair Display',serif;font-weight:900;line-height:.95;letter-spacing:-1px}
  .front-cover__title-main{display:block;font-size:76px}
  .front-cover__title-sub{display:block;font-size:64px}
  .front-cover__panels{position:absolute;left:0;top:225px;width:504px;height:410px}
  .front-cover__authors{position:absolute;left:0;top:652px;width:100%;text-align:center;color:var(--slate);
    font-family:'Playfair Display',serif;font-weight:700;font-size:25px;line-height:1.15;letter-spacing:.5px}
  .front-cover__authors small{display:block;font-size:20px;font-weight:600}
</style>
</head>
<body>
  <main class="spread">
    <section class="back-cover">
      <div class="back-cover__banner" role="img" aria-label="Blue-tinted photograph of relief aircraft over an old colonial map"></div>
      <figure class="back-cover__photo">
        <div class="back-cover__photo-fill" role="img" aria-label="Photograph of the authors talking beside a pond in the salt fields"></div>
      </figure>
      <div class="back-cover__blurb">
        <p class="back-cover__lead">Daravy's Tralonh – a modern history of the colourful Cambodian province of Tralonh, told through the lives of the salt fields tribe of Prey Ambel.</p>
        <p class="back-cover__body">Just outside of Tralonh town is the district of Prey Ambel, which contains hundreds of salt fields, fringed with small, basic houses and rice paddies. This book tells the stories of some of the resilient, resourceful and courageous people who have made their lives there.</p>
        <p class="back-cover__body">Based on both documentary research and individual interviews, Daravy's Tralonh provides some answers to those who are curious about what the southern most edge of Cambodia has been through during the last 200 years. Tralonh Province has been a land of bandits and pirates, insurrection and terrible brutality, pioneering agriculture and tribal enclaves, and colonialist endeavours and heroic resistance.</p>
        <p class="back-cover__body">In particular, the book follows the extended family of Daravy Po through the twentieth century to the present, including the catastrophic 1970s, when civil war and the Khmer Rouge dominated the province.</p>
        <p class="back-cover__body">Tralonh is being drawn rapidly into the technological new millennium but this book seeks to ensure its rich past is not forgotten.</p>
      </div>
    </section>

    <section class="spine">
      <div class="spine__title">DARAVY'S TRALONH</div>
      <div class="spine__authors">TOM HADLEY<br>WITH DARAVY PO</div>
    </section>

    <section class="front-cover">
      <h1 class="front-cover__title">
        <span class="front-cover__title-main">DARAVY'S</span>
        <span class="front-cover__title-sub">TRALONH</span>
      </h1>
      <svg class="front-cover__panels" viewBox="0 0 504 410">
        <defs>
          <linearGradient id="saltFields" x1="0" y1="0" x2="1" y2="0">
            <stop offset="0" stop-color="#b5553a"/>
            <stop offset=".3" stop-color="#4a78c4"/>
            <stop offset="1" stop-color="#3f8fd0"/>
          </linearGradient>
          <linearGradient id="oldMap" x1="0" y1="0" x2="1" y2="1">
            <stop offset="0" stop-color="#9fd2e6"/>
            <stop offset="1" stop-color="#7fc0da"/>
          </linearGradient>
          <linearGradient id="riverScene" x1="0" y1="0" x2="1" y2="1">
            <stop offset="0" stop-color="#4aa7de"/>
            <stop offset=".5" stop-color="#b4472f"/>
            <stop offset="1" stop-color="#3a9ad6"/>
          </linearGradient>
        </defs>
        <polygon role="img" aria-label="Coloured drawing of salt field workers carrying baskets" fill="url(#saltFields)" points="69,28 438,3 438,87 69,102"/>
        <polygon class="panel-divider" fill="var(--slate)" points="48,107 458,78 458,83 48,112"/>
        <polygon role="img" aria-label="French colonial street map of the town" fill="url(#oldMap)" points="48,112 458,83 458,216 48,242"/>
        <polygon class="panel-divider" fill="var(--slate)" points="48,242 458,216 458,221 48,247"/>
        <polygon role="img" aria-label="Coloured drawing of a river crossing with a red bridge" fill="url(#riverScene)" points="69,254 435,222 435,369 69,401"/>
      </svg>
      <p class="front-cover__authors">TOM HADLEY<small>WITH DARAVY PO</small></p>
    </section>
  </main>
</body>
</html>
```